Beacon Crest Service HVAC Card

Sale, Install, Maintenance Commercial Vent Hood, Ice Machine & Refrigeration
Air Conditioning Heating & Cooling

Industry/Entity Type

Air Conditioning

Contact Information for Business Card

Beacon Crest Service
2847 Marlowe Ave.
Del Rio Tx, 78840
Ph. (555) 482-7193 Tomas B. Villareal Owner
Ph. (555) 619-2084 Hugo Saldivar Tec.
E-mail. beaconcrest2847@mailbrook.example

```html
<!DOCTYPE html>
<html lang="en">
<head>
<meta charset="utf-8">
<title>Beacon Crest Service HVAC Card</title>
<link rel="stylesheet" href="https://fonts.googleapis.com/css2?family=Questrial&display=swap">
<style>
  :root {
    --page-bg: #36322e;
    --card-blue-light: #2fa3e6;
    --card-blue-mid: #1670c8;
    --card-blue-dark: #0b3f8c;
    --band-grey: #3d3d3f;
    --accent-red: #e4221c;
    --text-white: #ffffff;
  }
  html, body {
    margin: 0;
    padding: 0;
    width: 1200px;
    height: 917px;
    overflow: hidden;
    background: var(--page-bg);
  }
  .canvas {
    position: relative;
    width: 1200px;
    height: 917px;
  }
  .card {
    position: absolute;
    left: 250px;
    width: 700px;
    height: 400px;
    overflow: hidden;
    box-shadow: 0 10px 28px rgba(0,0,0,0.45);
  }
  .card--back { top: 38px; }
  .card--front { top: 479px; }
  .card svg { display: block; }
  .card-text {
    font-family: "Questrial", "Century Gothic", sans-serif;
    fill: var(--text-white);
  }
  .brand-name {
    font-family: "Questrial", "Century Gothic", sans-serif;
    fill: var(--accent-red);
    font-size: 44px;
  }
</style>
</head>
<body>
<main class="canvas">

  <!-- Back side: services -->
  <section class="card card--back" aria-label="Card back with services">
    <svg width="700" height="400" viewBox="0 0 700 400">
      <defs>
        <radialGradient id="back-glow" cx="0.42" cy="0.38" r="0.75">
          <stop offset="0" stop-color="var(--card-blue-light)"/>
          <stop offset="0.5" stop-color="var(--card-blue-mid)"/>
          <stop offset="1" stop-color="var(--card-blue-dark)"/>
        </radialGradient>
      </defs>
      <rect class="card-surface" width="700" height="400" fill="url(#back-glow)"/>
      <polygon class="card-band" points="338,400 700,126 700,212 452,400" fill="var(--band-grey)"/>
      <line class="card-rule" x1="322" y1="400" x2="700" y2="114" stroke="var(--accent-red)" stroke-width="3"/>
      <text class="card-text band-email" font-size="17" text-anchor="middle" transform="rotate(-37.1 575 270)" x="575" y="276">beaconcrest2847@mailbrook.example</text>
      <g class="card-text services" font-size="20" text-anchor="middle">
        <text x="270" y="150">Sale, Install, Maintenance Commercial Vent Hood,</text>
        <text x="270" y="179">Ice Machine &amp; Refrigeration</text>
        <text x="270" y="208">Air Conditioning Heating &amp; Cooling</text>
      </g>
    </svg>
  </section>

  <!-- Front side: name and contacts -->
  <section class="card card--front" aria-label="Card front with contact details">
    <svg width="700" height="400" viewBox="0 0 700 400">
      <defs>
        <radialGradient id="front-glow" cx="0.5" cy="0.6" r="0.8">
          <stop offset="0" stop-color="var(--card-blue-light)"/>
          <stop offset="0.5" stop-color="var(--card-blue-mid)"/>
          <stop offset="1" stop-color="var(--card-blue-dark)"/>
        </radialGradient>
      </defs>
      <rect class="card-surface" width="700" height="400" fill="url(#front-glow)"/>
      <polygon class="card-band" points="0,140 700,80 700,160 0,220" fill="var(--band-grey)"/>
      <line class="card-rule" x1="0" y1="132" x2="700" y2="72" stroke="var(--accent-red)" stroke-width="3"/>
      <line class="card-rule" x1="0" y1="228" x2="700" y2="168" stroke="var(--accent-red)" stroke-width="3"/>
      <text class="brand-name" x="350" y="165" text-anchor="middle" transform="rotate(-4.9 350 150)">Beacon Crest Service</text>
      <g class="card-text contacts" font-size="19" text-anchor="middle" transform="rotate(-4.9 350 300)">
        <text x="350" y="258">2847 Marlowe Ave. Brenmoor Tx. 79915</text>
        <text x="350" y="283">Ph. (555) 482-7193 Tomas B.</text>
        <text x="350" y="308">Villareal Owner Ph. (555) 619-2084</text>
        <text x="350" y="333">Hugo Saldivar Tec.</text>
        <text x="350" y="364">E-mail. beaconcrest2847@mailbrook.example</text>
      </g>
    </svg>
  </section>

</main>
</body>
</html>
```